Vantrell OBGYN Partners LLC
...connect the dots (docs!)
Vantrell OBGYN Partners LLC -
Creative Brief
Simple
Dr. Marlene Fostwick-Abara MD FACOG
2846 Quillan Avenue Suite 240 Tucker, Ga 30091
marlene@vantrellobgynpartners.example
www.vantrellobgynpartners.example
Desire same logo continued with above second line listed as in Hire-a-medic logo by KARBIMOSS design#12 with above adjustment in subtitle
Vantrell OBGYN Partners Locum tenens option for OBGYN's ...connect to us and we will help you connect the dots in your day!

```html
<!DOCTYPE html>
<html lang="en">
<head>
<meta charset="utf-8">
<title>Vantrell OBGYN Partners LLC – Business Cards</title>
<link href="https://fonts.googleapis.com/css2?family=Arimo:wght@400;700&display=swap" rel="stylesheet">
<style>
  :root {
    --backdrop: #e9e9e9;
    --card: #ffffff;
    --teal: #2fb4c2;
    --teal-light: #8fd6de;
    --magenta: #d9358a;
    --ink: #3d3d3d;
    --muted: #6a6a6a;
  }
  * { margin: 0; padding: 0; box-sizing: border-box; }
  html, body { width: 1200px; height: 1039px; overflow: hidden; }
  body {
    background: var(--backdrop);
    font-family: "Arimo", Arial, sans-serif;
    color: var(--ink);
    position: relative;
  }
  .card {
    position: absolute;
    left: 250px;
    width: 700px;
    height: 400px;
    background: var(--card);
    border-radius: 26px;
    overflow: hidden;
    box-shadow: 0 6px 18px rgba(0,0,0,.18);
  }
  .card--front { top: 90px; }
  .card--back { top: 550px; }

  .card__band {
    position: absolute;
    left: 0; bottom: 0;
    width: 100%;
    height: 70px;
  }

  .brand-name {
    color: var(--teal);
    font-weight: 400;
    letter-spacing: .2px;
  }
  .brand-tagline { color: var(--muted); }

  /* Front */
  .front__lockup {
    position: absolute;
    top: 128px; left: 0; width: 100%;
    text-align: center;
  }
  .front__lockup .brand-name { font-size: 38px; }
  .front__lockup .brand-tagline { font-size: 24px; margin-top: 4px; }
  .front__intro {
    position: absolute;
    left: 30px; top: 268px;
    font-size: 14px;
    line-height: 1.4;
    color: var(--ink);
  }

  /* Back */
  .back__lockup {
    position: absolute;
    left: 36px; top: 165px;
    width: 300px;
    text-align: center;
  }
  .back__lockup .brand-name { font-size: 25px; }
  .back__lockup .brand-tagline { font-size: 17px; margin-top: 3px; }

  .back__details {
    position: absolute;
    left: 348px; top: 108px;
    font-size: 16px;
    line-height: 1.35;
  }
  .back__company { color: var(--teal); font-size: 24px; font-weight: 700; }
  .back__doctor { font-size: 17px; margin-bottom: 30px; }
  .back__address { margin-bottom: 6px; }
  .contact-label { color: var(--teal); margin-right: 6px; }
  .back__url {
    position: absolute;
    left: 0; bottom: 18px; width: 100%;
    text-align: center;
    color: #fff;
    font-size: 17px;
  }
</style>
</head>
<body>

<section class="card card--front">
  <div class="front__lockup">
    <div class="brand-name">Vantrell OBGYN Partners LLC</div>
    <div class="brand-tagline">Connect the dots ( docs )</div>
  </div>
  <p class="front__intro">
    Vantrell OBGYN Partners<br>
    Locum tenens option for OBGYN's<br>
    ...connect to us and we will help you connect the dots in your day!
  </p>
  <svg class="card__band" viewBox="0 0 700 70" preserveAspectRatio="none" aria-hidden="true">
    <path d="M0 30 Q350 10 700 22 L700 70 L0 70 Z" fill="var(--teal-light)"/>
    <path d="M0 38 Q350 22 700 30 L700 70 L0 70 Z" fill="var(--teal)"/>
  </svg>
</section>

<section class="card card--back">
  <div class="back__lockup">
    <div class="brand-name">Vantrell OBGYN Partners LLC</div>
    <div class="brand-tagline">Connect the dots ( docs )</div>
  </div>
  <div class="back__details">
    <div class="back__company">Vantrell OBGYN Partners LLC</div>
    <div class="back__doctor">Dr. Marlene Fostwick-Abara MD FACOG</div>
    <div class="back__address">2846 Quillan Avenue<br>Suite 240 Tucker, Ga 30091</div>
    <div><span class="contact-label">p:</span>800.555.0147</div>
    <div><span class="contact-label">f:</span>888.555.0162</div>
    <div><span class="contact-label">e:</span>marlene@vantrellobgynpartners.example</div>
  </div>
  <svg class="card__band" viewBox="0 0 700 70" preserveAspectRatio="none" aria-hidden="true">
    <path d="M0 10 Q350 0 700 6 L700 70 L0 70 Z" fill="var(--teal-light)"/>
    <path d="M0 16 Q350 6 700 12 L700 70 L0 70 Z" fill="var(--teal)"/>
  </svg>
  <div class="back__url">www.vantrellobgynpartners.example</div>
</section>

</body>
</html>
```